Modern HomePage Design for Church

We are looking for a modern homepage design using the sections we put together in the template. The colors we want are blue, black, grey, and white. We do not want use the colors in the logo. Please modify the logo color to match the website color scheme.

Target Market(s)

Church

Industry/Entity Type

Church

Number of Pages Required

1 page

Colors
0293ce
ffffff
474747
9d9d9d

```html
<!DOCTYPE html>
<html lang="en">
<head>
<meta charset="utf-8">
<title>Wellspring Grace – Home</title>
<link rel="stylesheet" href="https://fonts.googleapis.com/css2?family=Montserrat:wght@400;500;600;700&family=Open+Sans:wght@400;600&family=Oswald:wght@300;400&family=Dancing+Script:wght@600&display=swap">
<style>
:root{
  --blue:#0293ce;
  --white:#ffffff;
  --charcoal:#474747;
  --grey:#9d9d9d;
  --ink:#2b2b2b;
  --panel:#3a3a3a;
  --light:#f0f0f0;
  --text:#555555;
}
*{box-sizing:border-box;margin:0;padding:0}
html,body{width:1200px;height:3371px;overflow:hidden}
body{position:relative;background:var(--white);font-family:"Open Sans",Arial,sans-serif;color:var(--text)}
section,header,footer,nav{position:absolute;left:0;width:1200px}
.abs{position:absolute}
.btn{position:absolute;display:flex;align-items:center;justify-content:center;font-family:"Montserrat",sans-serif;font-weight:600;font-size:9px;letter-spacing:.5px;text-transform:uppercase;color:var(--white)}
.btn-blue{background:var(--blue)}
.btn-grey{background:#7d7d7d;border:1px solid #6a6a6a}
.btn-outline{border:2px solid #333;color:#333;background:transparent}
.photo{position:absolute}

/* nav */
.top-nav{top:0;height:36px;background:var(--ink)}
.top-nav a{position:absolute;top:11px;font-family:"Montserrat",sans-serif;font-size:9px;color:#ddd;text-decoration:none;text-transform:uppercase;letter-spacing:.3px}
.top-nav a.active{color:var(--blue)}

/* hero */
.hero{top:36px;height:463px;background:radial-gradient(ellipse at 60% 40%,#3a3a3a,#232323)}
.brand{position:absolute;display:flex;align-items:center;gap:8px;font-family:"Montserrat",sans-serif;font-weight:600;color:var(--blue);text-transform:uppercase}
.brand .mark{width:12px;height:12px;background:var(--blue)}
.hero-tag{font-family:"Dancing Script",cursive;font-size:21px;line-height:26px;color:var(--white);width:100%;text-align:center;top:166px}
.hero-title{font-family:"Montserrat",sans-serif;font-weight:700;font-size:36px;line-height:42px;color:var(--blue);width:100%;text-align:center;top:192px;letter-spacing:1px}
.hero-sub{font-family:"Montserrat",sans-serif;font-weight:700;font-size:24px;line-height:30px;color:var(--white);width:100%;text-align:center;top:236px;letter-spacing:.5px}
.hero-note{font-family:"Montserrat",sans-serif;font-weight:600;font-size:13px;line-height:18px;color:var(--white);width:100%;text-align:center;top:270px}

.visit-strip{top:499px;height:31px;background:var(--blue)}
.visit-strip p{position:absolute;left:411px;top:8px;font-size:9px;color:var(--white)}
.visit-strip b{font-weight:600}

/* welcome */
.welcome{top:530px;height:364px;background:var(--white)}
.welcome h2{position:absolute;left:151px;top:70px;font-family:"Montserrat",sans-serif;font-weight:500;font-size:15px;color:#333}
.welcome .lead{position:absolute;left:151px;top:95px;font-size:10px;color:#666}
.welcome .rule{position:absolute;left:151px;top:120px;width:523px;height:1px;background:#ccc}
.welcome .copy{position:absolute;left:151px;width:530px;font-size:9.5px;line-height:15px;color:#888}

/* countdown */
.countdown{top:894px;height:189px;background:var(--charcoal)}
.countdown .box{position:absolute;left:151px;top:14px;width:898px;height:162px;background:var(--panel)}
.countdown h3{position:absolute;left:0;width:520px;top:46px;text-align:center;font-family:"Montserrat",sans-serif;font-weight:500;font-size:15px;color:var(--white)}
.countdown .date{position:absolute;left:0;width:520px;top:68px;text-align:center;font-size:8.5px;color:#bbb}
.countdown .desc{position:absolute;left:100px;width:320px;top:98px;text-align:center;font-size:8.5px;line-height:13px;color:#ddd}
.unit{position:absolute;top:20px;width:62px;text-align:center;color:var(--white);font-family:"Oswald",sans-serif}
.unit small{display:block;font-size:9px;font-weight:300;color:#ccc}
.unit strong{display:block;font-size:38px;font-weight:300;line-height:44px}
.unit-sep{position:absolute;top:20px;width:1px;height:55px;background:#777}

/* beliefs */
.beliefs{top:1083px;height:373px}
.beliefs .bg{position:absolute;inset:0;background:linear-gradient(180deg,#c9ced2,#dfe2e4 50%,#c3c8cc)}
.belief{position:absolute;top:60px;width:240px;text-align:center}
.belief svg{display:block;margin:0 auto}
.belief h4{margin-top:34px;font-family:"Montserrat",sans-serif;font-weight:500;font-size:12.5px;color:#333;letter-spacing:.5px}
.belief p{margin-top:10px;font-size:10.5px;line-height:12px;color:#333}

/* gallery */
.gallery{top:1456px;height:490px;background:var(--charcoal)}
.tile{position:absolute}
.tile-label{position:absolute;height:22px;padding:0 10px;display:flex;align-items:center;background:rgba(40,40,40,.85);font-size:8px;color:var(--white)}
.tile-label.blue{background:var(--blue)}
.blog-panel{position:absolute;left:748px;top:14px;width:452px;height:231px;background:var(--charcoal);text-align:center}
.blog-panel h3{margin-top:72px;font-family:"Montserrat",sans-serif;font-weight:600;font-size:17px;color:var(--white);letter-spacing:1px}
.blog-panel .bar{width:50px;height:1px;background:var(--white);margin:4px auto 0}
.blog-panel p{margin:14px auto 0;width:350px;font-size:10.5px;line-height:15px;color:var(--white)}
.pray-panel{position:absolute;left:748px;top:259px;width:452px;height:231px;background:#e9e9e9;text-align:center}
.pray-panel h3{margin-top:52px;font-family:"Montserrat",sans-serif;font-weight:500;font-size:16px;color:#333;letter-spacing:.5px}
.pray-panel p{margin:14px auto 0;width:360px;font-size:9.5px;line-height:15px;color:#666}

/* pastor */
.pastor{top:1946px;height:449px}
.pastor .bg{position:absolute;inset:0;background:linear-gradient(160deg,#4a4a4a,#353535 60%,#2d2d2d)}
.kicker{position:absolute;font-family:"Montserrat",sans-serif;font-weight:600;font-size:9px;color:var(--white);letter-spacing:1px;display:flex;align-items:center;gap:10px}
.kicker i{display:block;height:2px;background:var(--white)}
.quote-title{position:absolute;left:364px;top:121px;font-family:"Montserrat",sans-serif;font-weight:600;font-size:15px;color:var(--white);letter-spacing:.5px}
.quote-text{position:absolute;left:364px;top:150px;width:360px;font-size:8.5px;line-height:16px;color:#ddd}
.quote-name{position:absolute;left:364px;top:264px;font-size:10px;font-weight:600;color:var(--white)}
.podcast{position:absolute;left:748px;width:301px;height:70px;border-bottom:1px solid #666}
.podcast .play{position:absolute;left:0;top:0;width:43px;height:43px;border:1px solid #888;background:#555}
.podcast h5{position:absolute;left:65px;top:2px;font-family:"Montserrat",sans-serif;font-weight:600;font-size:9.5px;color:var(--white)}
.podcast .by{position:absolute;left:0;top:52px;font-size:9px;color:#ccc}
.podcast .by span{color:var(--blue)}

/* events */
.events{top:2395px;height:695px;background:var(--white)}
.events h2{position:absolute;top:70px;width:100%;text-align:center;font-family:"Montserrat",sans-serif;font-weight:600;font-size:18px;color:#222}
.events .sub{position:absolute;top:98px;width:100%;text-align:center;font-size:10px;color:#555}
.event{position:absolute;left:151px;width:898px;height:151px;background:var(--light)}
.event .pic{position:absolute;left:0;top:0;width:249px;height:151px}
.event .badge{position:absolute;left:215px;top:40px;width:61px;height:56px;background:var(--blue);color:var(--white);text-align:center}
.badge strong{display:block;margin-top:8px;font-family:"Montserrat",sans-serif;font-weight:700;font-size:15px}
.badge small{display:block;margin-top:6px;font-size:8px}
.event h4{position:absolute;left:298px;top:18px;font-family:"Montserrat",sans-serif;font-weight:600;font-size:13px;color:#333}
.event .row{position:absolute;left:298px;display:flex;align-items:center;gap:10px;font-size:9px;color:#555}
.event .row.link{color:var(--blue)}
.event .btn-outline{left:698px;top:62px;width:104px;height:24px}

/* footer */
.site-footer{top:3090px;height:281px;background:var(--ink)}
.col-head{position:absolute;top:34px;width:200px;text-align:center;font-family:"Montserrat",sans-serif;font-weight:500;font-size:10px;color:var(--white)}
.mini{position:absolute;display:flex;gap:10px;width:190px}
.mini .thumb{width:45px;height:45px;flex:none}
.mini h6{font-family:"Montserrat",sans-serif;font-weight:600;font-size:7.5px;color:var(--blue);text-transform:uppercase;line-height:10px}
.mini p{font-size:8px;line-height:11px;color:var(--white)}
.tags{position:absolute;left:499px;top:72px;width:200px;display:flex;flex-wrap:wrap;gap:5px}
.tags span{background:var(--blue);color:var(--white);font-size:7.5px;padding:3px 6px}
</style>
</head>
<body>

<nav class="top-nav">
  <a style="left:226px">Home</a>
  <a style="left:280px">Team</a>
  <a style="left:330px">Features</a>
  <a class="active" style="left:402px">Events</a>
  <a style="left:464px">Sermons</a>
  <a style="left:538px">Contacts</a>
  <a style="left:612px">Blog</a>
  <div class="btn btn-blue" style="left:899px;top:7px;width:72px;height:24px">Give Online</div>
</nav>

<header class="hero">
  <div class="photo" role="img" aria-label="Pink tulip with green stem on a dark background" style="left:0;top:0;width:393px;height:390px;background:radial-gradient(ellipse at 55% 45%,#e9a9c2 0,#c66f93 18%,rgba(60,90,40,.8) 34%,rgba(35,35,35,0) 62%)"></div>
  <div class="brand" style="left:225px;top:62px;font-size:19px">Wellspring Grace <span class="mark"></span></div>
  <div class="btn" style="left:737px;top:27px;width:108px;height:16px;background:#3a4d5c;font-size:7px">Sunday Worship 8:15</div>
  <div class="btn" style="left:863px;top:27px;width:110px;height:16px;background:#3a4d5c;font-size:7px">Sunday School (9h00)</div>
  <div class="abs hero-tag">A very special celebration is near</div>
  <div class="abs hero-title">EASTER WEEK</div>
  <div class="abs hero-sub">JOIN THE REMEMBRANCE</div>
  <div class="abs hero-note">Services starting at 19h00 daily</div>
  <div class="btn btn-blue" style="left:550px;top:312px;width:102px;height:27px;font-size:8px">Continue Reading</div>
</header>

<section class="visit-strip">
  <p><b>First time visitor?</b> .... Find out how, where and when we worship. We hope to see you soon!</p>
  <div class="btn" style="left:888px;top:5px;width:85px;height:21px;background:#2f2f2f;font-size:8px">Visitors Info</div>
</section>

<section class="welcome">
  <h2>Welcome to Riverstone Church</h2>
  <p class="lead">We are a community who firmly believes in God's word. Come journey with us.</p>
  <div class="rule"></div>
  <p class="copy" style="top:137px">Our doors are open to everyone seeking hope, rest and honest friendship. We gather each week to pray, to learn the Scriptures together and to serve our neighbours in practical ways.</p>
  <p class="copy" style="top:187px">Whether you have walked with faith for years or are only beginning to ask questions, there is a place for you here and a people ready to welcome you.</p>
  <div class="photo" role="img" aria-label="Handwritten pastor signature" style="left:191px;top:272px;width:146px;height:48px;background:linear-gradient(90deg,#eeeeee,#f7f7f7)"></div>
  <div class="photo" role="img" aria-label="Portrait of the pastor in a black clerical shirt" style="left:764px;top:23px;width:281px;height:341px;background:linear-gradient(180deg,#e8e8e8 0,#d9d9d9 40%,#2a2a2a 55%,#1c1c1c)"></div>
</section>

<section class="countdown">
  <div class="box">
    <h3>Church Leaders meeting</h3>
    <p class="date">March 27, 2018 7:00 pm</p>
    <p class="desc">Meeting for the church leaders. This is where we plan the strategy for the church and give feedback on projects</p>
    <div class="unit" style="left:490px"><small>Days</small><strong>06</strong></div>
    <div class="unit-sep" style="left:556px"></div>
    <div class="unit" style="left:552px"><small>Hours</small><strong>15</strong></div>
    <div class="unit-sep" style="left:618px"></div>
    <div class="unit" style="left:614px"><small>Minutes</small><strong>28</strong></div>
    <div class="unit-sep" style="left:680px"></div>
    <div class="unit" style="left:676px"><small>Seconds</small><strong>16</strong></div>
    <div class="btn btn-blue" style="left:599px;top:92px;width:75px;height:22px;font-size:8px">Read More</div>
  </div>
</section>

<section class="beliefs">
  <div class="bg" role="img" aria-label="Congregation raising hands in worship, softened under a light grey veil"></div>
  <div class="belief" style="left:228px">
    <svg width="80" height="70" viewBox="0 0 80 70"><path d="M40 68 L8 36 A18 18 0 0 1 40 10 A18 18 0 0 1 72 36 Z" fill="#0293ce"/></svg>
    <h4>WHAT WE BELIEVE</h4>
    <p>We believe in the existence of God<br>and His Holy Word to be the<br>foundation of our faith. It shall not<br>be moved nor be compromised.</p>
    <div class="btn btn-grey" style="left:78px;top:206px;width:84px;height:25px;position:absolute">Read More</div>
  </div>
  <div class="belief" style="left:480px">
    <svg width="80" height="70" viewBox="0 0 80 70"><circle cx="40" cy="35" r="34" fill="#0293ce"/><path d="M40 14 V36 L54 46" stroke="#fff" stroke-width="5" fill="none" stroke-linecap="round"/></svg>
    <h4>SERVICES &amp; LOCATION</h4>
    <p>Pinecrest, GA 30000, USA<br>Sunday Morning (8:15-12:00 AM)<br>Sunday Afternoon (4:00-6:00 PM)<br>Wednesday (8:00-9:00 PM)</p>
    <div class="btn btn-grey" style="left:78px;top:206px;width:84px;height:25px;position:absolute">Browse More</div>
  </div>
  <div class="belief" style="left:716px">
    <svg width="90" height="70" viewBox="0 0 90 70"><circle cx="56" cy="18" r="9" fill="#0293ce"/><path d="M6 50 Q22 36 40 42 L62 42 Q68 44 62 48 L44 50 L68 48 L86 34 Q90 36 86 42 L70 58 Q60 64 44 62 L12 62 Z" fill="#0293ce"/></svg>
    <h4>SERVICES &amp; LOCATION</h4>
    <p>Pinecrest, GA 30000, USA<br>Sunday Morning (8:15-12:00 AM)<br>Sunday Afternoon (4:00-6:00 PM)<br>Wednesday (8:00-9:00 PM)</p>
    <div class="btn btn-blue" style="left:78px;top:206px;width:84px;height:25px;position:absolute">Watch Live</div>
  </div>
</section>

<section class="gallery">
  <div class="tile" role="img" aria-label="Two children hugging outdoors" style="left:0;top:14px;width:364px;height:231px;background:linear-gradient(135deg,#6a4a2c,#b88a5a 50%,#4d3b28)"></div>
  <div class="tile-label" style="left:140px;top:204px">Kids Ministry</div>
  <div class="tile" role="img" aria-label="Hands folded in prayer over a book" style="left:373px;top:14px;width:175px;height:231px;background:linear-gradient(135deg,#2d2d2d,#6b5a4c 60%,#3a3a3a)"></div>
  <div class="tile-label" style="left:400px;top:204px">Outreach Ministry</div>
  <div class="tile" role="img" aria-label="Two teenagers talking and smiling" style="left:557px;top:14px;width:180px;height:231px;background:linear-gradient(135deg,#e9e9e9,#c9a27a 50%,#e0c23c)"></div>
  <div class="tile-label" style="left:600px;top:204px">Teens Ministry</div>
  <div class="blog-panel">
    <h3>BLOG</h3><div class="bar"></div>
    <p>The success of our Church depends on participation from people like you. Get involved in our Ministries - it will change your life.</p>
  </div>

  <div class="tile" role="img" aria-label="Elderly couple embracing" style="left:0;top:259px;width:175px;height:231px;background:linear-gradient(135deg,#8aa07a,#c8c2b8 50%,#5c6e52)"></div>
  <div class="tile-label" style="left:36px;top:442px">Seniors Ministry</div>
  <div class="tile" role="img" aria-label="Holy Bible on a wooden table" style="left:187px;top:259px;width:177px;height:231px;background:linear-gradient(135deg,#6b4a33,#2a211b 55%,#8c6a4c)"></div>
  <div class="tile-label blue" style="left:225px;top:442px">Bible Study</div>
  <div class="tile" role="img" aria-label="Child on a swing in a green park" style="left:373px;top:259px;width:364px;height:231px;background:linear-gradient(180deg,#3f6a2c,#7da35a 60%,#5a7c3c)"></div>
  <div class="tile-label" style="left:505px;top:442px">Kids Ministry</div>
  <div class="pray-panel">
    <h3>PRAY WITHOUT CEASING</h3>
    <p>Lift every worry and every joy to God in prayer. Our prayer team meets each week and would love to stand with you, whatever season you are walking through right now.</p>
    <div class="btn btn-outline" style="left:175px;top:134px;width:104px;height:22px">Read More</div>
  </div>
</section>

<section class="pastor">
  <div class="bg" role="img" aria-label="Open Bible in dim light behind a dark overlay"></div>
  <div class="kicker" style="left:151px;top:92px"><i style="width:60px"></i>PASTOR</div>
  <div class="photo" role="img" aria-label="Portrait of the pastor with a beard" style="left:151px;top:121px;width:186px;height:252px;background:linear-gradient(180deg,#d8d8d8,#b9a898 50%,#5a5550)"></div>
  <div class="quote-title">“ONE THING I ASK OF THE LORD”</div>
  <p class="quote-text">This week I seek: that I may dwell in the house of the Lord all the days of my life, to gaze upon the beauty of the Lord and to seek Him in His temple. Taste and see that the Lord is good; blessed is the man who takes refuge in Him. The Lord is everlasting God, the creator of the ends of the earth.</p>
  <div class="quote-name">Daniel Hartwell</div>
  <div class="kicker" style="left:748px;top:92px"><i style="width:70px"></i>PODCASTS<i style="width:150px"></i></div>
  <div class="podcast" style="top:121px"><div class="play"></div><h5>HOLY SPIRIT: STRATEGIC THINKIG</h5><p class="by">by <span>Mara Ellison</span></p></div>
  <div class="podcast" style="top:211px"><div class="play"></div><h5>HOLY SPIRIT: STRATEGIC THINKIG</h5><p class="by">by <span>Mara Ellison</span></p></div>
  <div class="podcast" style="top:301px"><div class="play"></div><h5>HOLY SPIRIT: STRATEGIC THINKIG</h5><p class="by">by <span>Mara Ellison</span></p></div>
</section>

<section class="events">
  <h2>UPCOMING EVENTS</h2>
  <p class="sub">Experience God's Presence</p>

  <article class="event" style="top:146px">
    <div class="pic" role="img" aria-label="Little girl smiling" style="background:linear-gradient(135deg,#4a3a30,#b58a6c 55%,#3d2f28)"></div>
    <div class="badge"><strong>22nd</strong><small>Feb 2018</small></div>
    <h4>Sharing Our Love &amp; faith To Children</h4>
    <div class="row" style="top:50px"><svg width="12" height="12" viewBox="0 0 12 12"><rect x="1" y="2" width="10" height="9" fill="none" stroke="#0293ce"/><path d="M1 5h10" stroke="#0293ce"/></svg>Thursday, 08:00 am - Thursday, 09:00 am</div>
    <div class="row link" style="top:78px"><svg width="12" height="12" viewBox="0 0 12 12"><path d="M6 11 C2 6 2 4 2 4 A4 4 0 0 1 10 4 C10 4 10 6 6 11Z" fill="#0293ce"/></svg>St. Meadowbrook Church</div>
    <div class="row" style="top:106px"><svg width="12" height="12" viewBox="0 0 12 12"><path d="M11 1 L1 5 L5 7 L7 11Z" fill="#0293ce"/></svg>Elm Row, Harborview, United States, 10000</div>
    <div class="btn btn-outline">Read More</div>
  </article>

  <article class="event" style="top:308px">
    <div class="pic" role="img" aria-label="Rows of red candles burning" style="background:linear-gradient(135deg,#2a0a0a,#b8221c 50%,#3c0c0a)"></div>
    <div class="badge"><strong>22nd</strong><small>Feb 2018</small></div>
    <h4>Know Jesus Christ Better Through lines</h4>
    <div class="row" style="top:50px"><svg width="12" height="12" viewBox="0 0 12 12"><rect x="1" y="2" width="10" height="9" fill="none" stroke="#0293ce"/><path d="M1 5h10" stroke="#0293ce"/></svg>Thursday, 08:00 am - Thursday, 09:00 am</div>
    <div class="row link" style="top:78px"><svg width="12" height="12" viewBox="0 0 12 12"><path d="M6 11 C2 6 2 4 2 4 A4 4 0 0 1 10 4 C10 4 10 6 6 11Z" fill="#0293ce"/></svg>St. Meadowbrook Church</div>
    <div class="row" style="top:106px"><svg width="12" height="12" viewBox="0 0 12 12"><path d="M11 1 L1 5 L5 7 L7 11Z" fill="#0293ce"/></svg>Maple Hollow Lane, Brookfield, Kentucky, United States, 40100</div>
    <div class="btn btn-outline">Read More</div>
  </article>

  <article class="event" style="top:470px">
    <div class="pic" role="img" aria-label="Crowd gathered outdoors under trees at sunset" style="background:linear-gradient(180deg,#c9b48a,#7a8a4c 55%,#3c4a2a)"></div>
    <div class="badge"><strong>21st</strong><small>Feb 2018</small></div>
    <h4>Caring About The Community &amp; Serving</h4>
    <div class="row" style="top:50px"><svg width="12" height="12" viewBox="0 0 12 12"><rect x="1" y="2" width="10" height="9" fill="none" stroke="#0293ce"/><path d="M1 5h10" stroke="#0293ce"/></svg>Wednesday, 08:00 am - Thursday, 09:00 am</div>
    <div class="row link" style="top:78px"><svg width="12" height="12" viewBox="0 0 12 12"><path d="M6 11 C2 6 2 4 2 4 A4 4 0 0 1 10 4 C10 4 10 6 6 11Z" fill="#0293ce"/></svg>St. Meadowbrook Church</div>
    <div class="row" style="top:106px"><svg width="12" height="12" viewBox="0 0 12 12"><path d="M11 1 L1 5 L5 7 L7 11Z" fill="#0293ce"/></svg>Cedar Ridge Road, Fairmount, Kentucky, United States, 42000</div>
    <div class="btn btn-outline">Read More</div>
  </article>
</section>

<footer class="site-footer">
  <div class="col-head" style="left:251px">Latest Sermons</div>
  <div class="col-head" style="left:500px">Sermon Tags</div>
  <div class="col-head" style="left:745px">Latest news</div>

  <div class="mini" style="left:254px;top:70px"><div class="thumb" role="img" aria-label="Speaker portrait" style="background:linear-gradient(#888,#444)"></div><div><h6>All things are possible</h6><p>Lorem ipsum dolor sit amet, consectetur...</p></div></div>
  <div class="mini" style="left:254px;top:128px"><div class="thumb" role="img" aria-label="Speaker portrait" style="background:linear-gradient(#888,#444)"></div><div><h6>Abounding in the work of the Lord</h6><p>Lorem ipsum dolor sit amet, consectetur...</p></div></div>

  <div class="tags"><span>goodheartedness</span><span>faith</span><span>forgiveness</span><span>kidness</span><span>kindness</span><span>love</span><span>peace</span><span>understanding</span></div>

  <div class="mini" style="left:753px;top:70px"><div class="thumb" role="img" aria-label="News photo" style="background:linear-gradient(#6a5a5a,#3a2a2a)"></div><div><h6>Clocking keeps the blues away</h6><p>Lorem ipsum dolor sit amet, consectetur...</p></div></div>
  <div class="mini" style="left:753px;top:128px"><div class="thumb" role="img" aria-label="News photo" style="background:linear-gradient(#8a5a3a,#3a2a1a)"></div><div><h6>Blog posts are all the rage</h6><p>Lorem ipsum dolor sit amet, consectetur...</p></div></div>

  <div class="brand" style="left:0;width:1200px;justify-content:center;top:214px;font-size:20px">Wellspring Grace <span class="mark"></span></div>
</footer>

</body>
</html>
```